BRIGHTWATER RV Resort needs a logo and advertising poster

We need an advertising poster for our epic RV Resort located on north end of Tuskin Lake, (Northern Saskatchewan, trees no mountains)
SEASONAL FULL SERVICE SITES with marina and lake access.
Sauna/plunge, disc golf , hiking/quad trails, and pet friendly.
We are after a fun 70,s themed simple poster. Please use brand guide for colours and redo logo to be Brightwater Resort.

Target Market(s)

RV owners looking for permeant sites. No tenting.

Font styles to use
Other font styles liked:
• See brand guide

Requirements
Must have
• Change exisiting branding to BRIGHTWATER RESORT instead of coffee Emphasis Limited sites.... Referral discount. Phone number.
Nice to have
• .
Should not have
• Keep it simple

```html
<!DOCTYPE html>
<html lang="en">
<head>
<meta charset="utf-8">
<title>Tuskin Lake – Brightwater Resort</title>
<link rel="stylesheet" href="https://fonts.googleapis.com/css2?family=Bowlby+One&family=Poppins:wght@400;500;600;800&display=swap">
<style>
  :root {
    --paper: #f8f6e9;
    --title-green: #6a8450;
    --salmon: #d98770;
    --rust: #9a3a1e;
    --ink: #1c1c1c;
    --tick-green: #5e7a4a;
    --mint: #8fc7bd;
    --mustard: #e9c76a;
    --divider: #3a3a3a;
    --scene-sky: #62b5b0;
    --scene-sky-soft: #8cc4b8;
    --scene-sun: #f2dab2;
    --scene-forest: #4f7266;
    --scene-grass: #7aa466;
    --scene-grass-deep: #6a975a;
  }
  * { margin: 0; padding: 0; box-sizing: border-box; }
  html, body { width: 930px; height: 1200px; overflow: hidden; background: var(--paper); }
  .poster { position: relative; width: 930px; height: 1200px; background: var(--paper); font-family: "Poppins", sans-serif; }

  .headline { position: absolute; top: 64px; left: 0; width: 930px; text-align: center; }
  .headline__main { font-family: "Bowlby One", sans-serif; color: var(--title-green); font-size: 56px; line-height: 66px; letter-spacing: 0.5px; }
  .headline__sub { margin-top: 4px; color: var(--salmon); font-weight: 500; font-size: 44px; line-height: 54px; }

  .scene { position: absolute; left: 60px; top: 276px; width: 812px; height: 640px; }
  .scene svg { display: block; width: 100%; height: 100%; }

  .offer { position: absolute; left: 71px; top: 960px; width: 500px; }
  .offer__title { color: var(--rust); font-weight: 800; font-size: 22px; line-height: 31px; text-transform: uppercase; }
  .amenities { list-style: none; display: grid; grid-template-columns: 141px 166px 170px; row-gap: 2px; margin-top: 12px; }
  .amenities li { display: flex; align-items: center; font-size: 25px; line-height: 32px; color: var(--ink); }
  .amenities svg { width: 22px; height: 20px; margin-right: 8px; flex: none; }

  .contact { position: absolute; left: 71px; top: 1108px; display: flex; align-items: center; gap: 14px; font-weight: 600; font-size: 14.5px; color: var(--ink); }
  .brand { display: flex; align-items: center; gap: 6px; color: var(--title-green); font-weight: 800; font-size: 13px; line-height: 14px; }
  .brand__mark { width: 14px; height: 14px; border: 2px solid var(--title-green); border-radius: 3px; }
  .contact__item { display: flex; align-items: center; gap: 5px; }
  .contact__item svg { width: 15px; height: 15px; }

  .divider { position: absolute; left: 582px; top: 956px; width: 1px; height: 184px; background: var(--divider); }

  .deal { position: absolute; left: 611px; top: 960px; width: 250px; }
  .deal__label { font-weight: 600; font-size: 33px; line-height: 40px; color: var(--ink); padding-left: 4px; }
  .deal__amount { font-weight: 800; font-size: 122px; line-height: 100px; color: var(--mint); padding-left: 2px; letter-spacing: -2px; }
  .deal__tag { margin-top: 4px; width: 243px; height: 36px; background: var(--mustard); color: var(--rust); font-weight: 800; font-size: 23px; line-height: 36px; text-align: center; }
</style>
</head>
<body>
<main class="poster">
  <header class="headline">
    <h1 class="headline__main">TUSKIN LAKE IN<br>BRIGHTWATER RESORT</h1>
    <p class="headline__sub">and Marina development</p>
  </header>

  <div class="scene" role="img" aria-label="Retro illustration of a pine forest against a large pale sun, with a red tent and an orange 70s camper van on a grassy campsite">
    <svg viewBox="0 0 812 640" preserveAspectRatio="none" aria-hidden="true">
      <defs>
        <linearGradient id="scene-tones" x1="0" y1="0" x2="0" y2="1">
          <stop offset="0" stop-color="var(--scene-sky)"/>
          <stop offset="0.22" stop-color="var(--scene-sky-soft)"/>
          <stop offset="0.45" stop-color="var(--scene-sun)"/>
          <stop offset="0.66" stop-color="var(--scene-forest)"/>
          <stop offset="0.82" stop-color="var(--scene-grass)"/>
          <stop offset="1" stop-color="var(--scene-grass-deep)"/>
        </linearGradient>
        <radialGradient id="scene-glow" cx="0.5" cy="0.36" r="0.38">
          <stop offset="0" stop-color="var(--scene-sun)" stop-opacity="0.85"/>
          <stop offset="1" stop-color="var(--scene-sun)" stop-opacity="0"/>
        </radialGradient>
      </defs>
      <path d="M400 6C520 -6 600 40 662 108C722 168 778 250 792 340C815 420 812 520 802 600C700 640 520 640 380 626C240 616 122 602 60 560C20 522 30 470 14 420C-4 340 30 250 90 170C170 70 280 18 400 6Z" fill="url(#scene-tones)"/>
      <path d="M400 6C520 -6 600 40 662 108C722 168 778 250 792 340C815 420 812 520 802 600C700 640 520 640 380 626C240 616 122 602 60 560C20 522 30 470 14 420C-4 340 30 250 90 170C170 70 280 18 400 6Z" fill="url(#scene-glow)"/>
    </svg>
  </div>

  <section class="offer">
    <h2 class="offer__title">We provide seasonal full service<br>site with marina and lake access</h2>
    <ul class="amenities">
      <li><svg viewBox="0 0 22 20"><path d="M2 11l6 6L20 3" fill="none" stroke="var(--tick-green)" stroke-width="3" stroke-linecap="round" stroke-linejoin="round"/></svg>Sauna</li>
      <li><svg viewBox="0 0 22 20"><path d="M2 11l6 6L20 3" fill="none" stroke="var(--tick-green)" stroke-width="3" stroke-linecap="round" stroke-linejoin="round"/></svg>Disc golf</li>
      <li><svg viewBox="0 0 22 20"><path d="M2 11l6 6L20 3" fill="none" stroke="var(--tick-green)" stroke-width="3" stroke-linecap="round" stroke-linejoin="round"/></svg>Quad trails</li>
      <li><svg viewBox="0 0 22 20"><path d="M2 11l6 6L20 3" fill="none" stroke="var(--tick-green)" stroke-width="3" stroke-linecap="round" stroke-linejoin="round"/></svg>Plunge</li>
      <li><svg viewBox="0 0 22 20"><path d="M2 11l6 6L20 3" fill="none" stroke="var(--tick-green)" stroke-width="3" stroke-linecap="round" stroke-linejoin="round"/></svg>Hiking</li>
      <li><svg viewBox="0 0 22 20"><path d="M2 11l6 6L20 3" fill="none" stroke="var(--tick-green)" stroke-width="3" stroke-linecap="round" stroke-linejoin="round"/></svg>Pet friendly</li>
    </ul>
  </section>

  <footer class="contact">
    <div class="brand"><span class="brand__mark"></span><span>BRIGHTWATER<br>RESORT</span></div>
    <span class="contact__item">
      <svg viewBox="0 0 16 16"><circle cx="8" cy="8" r="7.5" fill="var(--title-green)"/><path d="M5.3 4.5l1.4-.3.8 1.8-.9.7c.4.9 1 1.5 1.9 1.9l.7-.9 1.8.8-.3 1.4c-3 .2-5.6-2.4-5.4-5.4z" fill="var(--paper)"/></svg>
      306-555-0142
    </span>
    <span class="contact__item">
      <svg viewBox="0 0 16 16"><circle cx="8" cy="8" r="7.5" fill="var(--title-green)"/><circle cx="8" cy="8" r="4.5" fill="none" stroke="var(--paper)" stroke-width="1"/><path d="M3.5 8h9M8 3.5c-2 2.5-2 6.5 0 9M8 3.5c2 2.5 2 6.5 0 9" fill="none" stroke="var(--paper)" stroke-width="1"/></svg>
      WWW.BRIGHTWATERRV.COM
    </span>
  </footer>

  <div class="divider"></div>

  <aside class="deal">
    <p class="deal__label">Limited sites</p>
    <p class="deal__amount">5%</p>
    <p class="deal__tag">referral discount</p>
  </aside>
</main>
</body>
</html>
```